Ochre Ridge Critters business card and social media card

I would like 2 designs,

one with my logo that I have (attached file) for the front and then the chatterbook, Snapwall and roamrater icons on the back.I would like it to be eye catching.

The second design i would like the designers to come up with.I am looking for a colorful and eye catching but easy to read business card. I am in the center of Australia and would like earthy colors like orange/red, yellow, charcoal, brown, green etc. I would like a blue tongue lizard and a king brown snake in the design for the front. For the back I would like the Chatterbook, Snapwall and roam rater logos.

Industry/Entity Type

Business

Contact Information for Business Card

Milo Farrant
CEO
OCHRE RIDGE CRITTERS pty ltd
W: 041 902 7364
M: 048 516 2097
E: milo@ochreridgecritters.com.au

Font styles to use
Other font styles liked:
• chiller

Colors
f37122
fbed22
ec1f27
474747
0492cd
acd036

Requirements
Must have
• Business name or my logo (attached file)
• Ochre Ridge Critters (in a cool font, like "chiller")
• Chatterbook icon
• Snapwall icon
• Roamrater icon
Nice to have
• Snake and a blue tongue lizard (either the full animals or just the heads)

```html
<!DOCTYPE html>
<html lang="en">
<head>
<meta charset="utf-8">
<title>Ochre Ridge Critters – Business Card</title>
<link href="https://fonts.googleapis.com/css2?family=Creepster&family=Open+Sans:wght@400;600&display=swap" rel="stylesheet">
<style>
  :root {
    --stage: #101010;
    --card: #ffffff;
    --red: #ec1f27;
    --orange: #f37122;
    --charcoal: #474747;
    --blue: #0492cd;
    --mist: #eceeee;
    --ink: #2b2b2b;
  }
  * { box-sizing: border-box; margin: 0; padding: 0; }
  html, body { width: 1200px; height: 1000px; overflow: hidden; background: var(--stage); }
  .stage { position: relative; width: 1200px; height: 1000px; }

  .card {
    position: absolute;
    width: 500px;
    height: 290px;
    background: var(--card);
    border-radius: 18px;
    overflow: hidden;
    font-family: "Open Sans", sans-serif;
  }
  .card--contact { left: 70px; top: 220px; }
  .card--brand { left: 630px; top: 450px; }

  /* contact side */
  .map-shade {
    position: absolute;
    right: 0; top: 40px;
    width: 250px; height: 200px;
    background: var(--mist);
    border-radius: 40% 20% 35% 45% / 35% 40% 30% 50%;
  }
  .holder { position: absolute; left: 40px; top: 22px; }
  .holder__name {
    font-family: "Creepster", cursive;
    color: var(--red);
    font-size: 28px;
    letter-spacing: 1px;
    line-height: 1;
  }
  .holder__role { font-size: 12px; color: var(--ink); margin-top: 2px; }

  .contact-list { position: absolute; left: 22px; top: 80px; list-style: none; }
  .contact-list li {
    display: flex; align-items: center; gap: 8px;
    font-size: 13px; color: var(--ink); height: 22px;
  }
  .contact-icon { width: 14px; height: 14px; flex: none; }

  .company-band {
    position: absolute;
    left: 0; top: 160px;
    width: 300px; height: 42px;
    background: var(--red);
    display: flex; align-items: center;
    padding-left: 20px;
  }
  .company-band__name {
    font-family: "Creepster", cursive;
    color: #fff;
    font-size: 18px;
    letter-spacing: 1px;
    white-space: nowrap;
  }

  .socials {
    position: absolute; right: 18px; bottom: 22px;
    display: flex; gap: 12px; list-style: none;
  }
  .socials li { display: flex; align-items: center; gap: 5px; font-size: 12px; font-weight: 600; color: var(--ink); }
  .socials .dot { width: 18px; height: 18px; border: 2px solid var(--ink); border-radius: 50%; }

  /* brand side */
  .stripes { position: absolute; inset: 0; }
  .map-cutout {
    position: absolute;
    left: 120px; top: 40px;
    width: 270px; height: 220px;
    background: var(--card);
    border-radius: 35% 45% 40% 30% / 40% 35% 45% 40%;
  }
  .brand-name {
    position: absolute;
    left: 150px; top: 100px;
    width: 210px;
    text-align: center;
    font-family: "Creepster", cursive;
    color: var(--red);
    font-size: 30px;
    line-height: 1.05;
    letter-spacing: 1px;
  }
</style>
</head>
<body>
<main class="stage">

  <section class="card card--contact">
    <div class="map-shade" role="img" aria-label="Faint grey map of Australia"></div>

    <div class="holder">
      <h1 class="holder__name">MILO FARRANT</h1>
      <p class="holder__role">CEO</p>
    </div>

    <ul class="contact-list">
      <li>
        <svg class="contact-icon" viewBox="0 0 14 14"><circle cx="7" cy="7" r="7" fill="var(--blue)"/><path d="M4.5 3.5l1.5 0 .6 2-1 .7a5 5 0 0 0 2.2 2.2l.7-1 2 .6 0 1.5c-3.5.3-6.3-2.5-6-6z" fill="#fff"/></svg>
        041 902 7364
      </li>
      <li>
        <svg class="contact-icon" viewBox="0 0 14 14"><circle cx="7" cy="7" r="7" fill="var(--blue)"/><rect x="5" y="3" width="4" height="8" rx="1" fill="#fff"/></svg>
        048 516 2097
      </li>
      <li>
        <svg class="contact-icon" viewBox="0 0 14 14"><circle cx="7" cy="7" r="7" fill="var(--blue)"/><rect x="3.5" y="4.5" width="7" height="5" fill="#fff"/><path d="M3.5 4.5l3.5 3 3.5-3" stroke="var(--blue)" stroke-width="1" fill="none"/></svg>
        milo@ochreridgecritters.com.au
      </li>
    </ul>

    <div class="company-band">
      <span class="company-band__name">OCHRE RIDGE CRITTERS pty ltd</span>
    </div>

    <ul class="socials">
      <li><span class="dot"></span>Roamrater</li>
      <li><span class="dot"></span>Chatterbook</li>
      <li><span class="dot"></span>Snapwall</li>
    </ul>
  </section>

  <section class="card card--brand">
    <svg class="stripes" viewBox="0 0 500 290" aria-hidden="true">
      <g transform="rotate(-35 250 145)">
        <rect x="-300" y="40" width="1100" height="48" fill="var(--blue)"/>
        <rect x="-300" y="88" width="1100" height="48" fill="var(--charcoal)"/>
        <rect x="-300" y="136" width="1100" height="48" fill="var(--orange)"/>
        <rect x="-300" y="184" width="1100" height="48" fill="var(--red)"/>
      </g>
    </svg>
    <div class="map-cutout" role="img" aria-label="White map of Australia"></div>
    <p class="brand-name">OCHRE RIDGE CRITTERS</p>
  </section>

</main>
</body>
</html>
```